Cool modern, tech Business card design

Looking for a new business card design for our Managed IT Services company. We would like 2 sides, with the logo one one side horizontally and then the information on the back in either vertical or horizontal. We want our colors from the logo incorporated but also would like to see the color gray in there as well.

Target Market(s)

IT, Information Technology, Tech, Service

Industry/Entity Type

It Service

Contact Information for Business Card

Carl Penner
Managing Partner
(P)555-271-4830 ext xxx
(F)555-271-4831
www.brixtelcore.com

Font styles to use
Sans Serif

Colors
959595
000000
ec1f27

Requirements
Must have
• Logo on one side with some nice design or pattern
• Information on back in either vertical or horizontal format
Nice to have
• For it to look cool, tech, modern, stand out.

```html
<!DOCTYPE html>
<html lang="en">
<head>
<meta charset="utf-8">
<title>Brixtelcore Business Card</title>
<link rel="stylesheet" href="https://fonts.googleapis.com/css2?family=Montserrat:wght@500;600;700;800&display=swap">
<style>
  :root {
    --brand-red: #ec1f27;
    --brand-red-deep: #b3141a;
    --brand-black: #000000;
    --brand-gray: #959595;
    --stage-gray: #8c8c8e;
    --paper: #ffffff;
  }
  * { margin: 0; padding: 0; box-sizing: border-box; }
  html, body {
    width: 1200px; height: 1200px; overflow: hidden;
    background: var(--stage-gray);
    font-family: "Montserrat", sans-serif;
  }
  .canvas { position: relative; width: 1200px; height: 1200px; }
  .card {
    position: absolute; left: 250px; width: 700px; height: 400px;
    background: var(--paper); overflow: hidden;
  }
  .card-front { top: 119px; }
  .card-back { top: 622px; }
  .card-art { position: absolute; inset: 0; width: 700px; height: 400px; }

  .brand {
    position: absolute; left: 0; right: 0; top: 150px;
    display: flex; justify-content: center; align-items: center; gap: 16px;
  }
  .brand-dot {
    width: 22px; height: 22px; border-radius: 50%; background: var(--brand-gray);
  }
  .brand-name {
    font-weight: 600; font-size: 54px; letter-spacing: 1px; line-height: 1;
    color: var(--brand-black);
  }

  .identity { position: absolute; left: 30px; top: 150px; width: 236px; text-align: center; }
  .person-name {
    font-weight: 800; font-size: 28px; letter-spacing: 1px; line-height: 1.1;
    color: var(--brand-black); text-transform: uppercase;
  }
  .person-role {
    margin-top: 4px; font-weight: 700; font-size: 16px; letter-spacing: 0.5px;
    color: var(--brand-black);
  }
  .identity-rule { display: flex; height: 5px; margin-top: 8px; }
  .identity-rule .rule-red { width: 42%; background: var(--brand-red); }
  .identity-rule .rule-black { flex: 1; height: 2px; margin-top: 1.5px; background: var(--brand-black); }

  .contact-list {
    position: absolute; left: 346px; top: 124px; list-style: none;
    display: flex; flex-direction: column; gap: 15px;
  }
  .contact-item {
    display: flex; align-items: center; gap: 14px;
    color: var(--paper); font-weight: 500; font-size: 26px; line-height: 40px;
  }
  .contact-item.web { font-size: 22px; }
  .contact-icon { width: 32px; height: 32px; flex: none; }
</style>
</head>
<body>
<main class="canvas">

  <section class="card card-front" aria-label="Front of business card">
    <svg class="card-art" viewBox="0 0 700 400" aria-hidden="true">
      <rect x="0" y="297" width="700" height="56" fill="var(--brand-black)"/>
      <polygon fill="var(--brand-red-deep)" points="0,168 60,190 0,206"/>
      <polygon fill="var(--brand-red)" points="0,112 236,400 172,400 0,190"/>
      <polygon fill="var(--brand-red-deep)" points="700,168 640,190 700,206"/>
      <polygon fill="var(--brand-red)" points="700,112 464,400 528,400 700,190"/>
    </svg>
    <div class="brand">
      <span class="brand-name">Brixtelcore</span>
      <span class="brand-dot"></span>
    </div>
  </section>

  <section class="card card-back" aria-label="Back of business card">
    <svg class="card-art" viewBox="0 0 700 400" aria-hidden="true">
      <rect x="306" y="0" width="394" height="400" fill="var(--brand-black)"/>
      <polygon fill="var(--brand-red)" points="306,0 470,0 345,110 306,110"/>
      <polygon fill="var(--brand-red-deep)" points="306,110 345,110 306,145"/>
      <polygon fill="var(--brand-red)" points="306,400 470,400 345,290 306,290"/>
      <polygon fill="var(--brand-red-deep)" points="306,290 345,290 306,255"/>
    </svg>

    <div class="identity">
      <p class="person-name">Carl Penner</p>
      <p class="person-role">Managing Partner</p>
      <div class="identity-rule"><span class="rule-red"></span><span class="rule-black"></span></div>
    </div>

    <ul class="contact-list">
      <li class="contact-item">
        <svg class="contact-icon" viewBox="0 0 34 34" aria-label="Phone">
          <circle cx="17" cy="17" r="16" fill="var(--paper)"/>
          <path d="M11 9.5l3.5-.5 2 4.5-2.2 1.6a10 10 0 0 0 4.6 4.6l1.6-2.2 4.5 2-.5 3.5c-7 .5-14-6.5-13.5-13.5z" fill="var(--brand-black)"/>
        </svg>
        <span>(555) 271-4830</span>
      </li>
      <li class="contact-item">
        <svg class="contact-icon" viewBox="0 0 34 34" aria-label="Fax">
          <circle cx="17" cy="17" r="16" fill="var(--paper)"/>
          <rect x="12" y="8" width="10" height="6" fill="var(--brand-black)"/>
          <rect x="8" y="14" width="18" height="10" rx="2" fill="var(--brand-black)"/>
          <rect x="12" y="20" width="10" height="6" fill="var(--brand-black)" stroke="var(--paper)" stroke-width="1.5"/>
        </svg>
        <span>(555) 271-4831</span>
      </li>
      <li class="contact-item web">
        <svg class="contact-icon" viewBox="0 0 34 34" aria-label="Website">
          <circle cx="17" cy="17" r="16" fill="var(--paper)"/>
          <g fill="none" stroke="var(--brand-black)" stroke-width="1.8">
            <circle cx="17" cy="17" r="9"/>
            <ellipse cx="17" cy="17" rx="4" ry="9"/>
            <line x1="8" y1="17" x2="26" y2="17"/>
          </g>
        </svg>
        <span>www.brixtelcore.com</span>
      </li>
    </ul>
  </section>

</main>
</body>
</html>
```